Coffee 317 Q-Pod

We have recently launched a coffee company called Lumo 317 that provides clean water and economic empowerment to Hondurans. It is premium direct trade coffee. We are looking for a very clean, professional looking box for our Q-Pods. I'm uploading a logo, what we are thinking so far, and an example of a dapple dough q pod box that I liked, but if you can think of a better design, please submit it. I'm not tied to anything that I uploaded. Please submit the artwork in a similiar format to diagram with the outline of the print out.

```html
<!DOCTYPE html>
<html lang="en">
<head>
<meta charset="utf-8">
<title>Lumo 317 Signature Roast – Q-Pod Box Dieline</title>
<link rel="stylesheet" href="https://fonts.googleapis.com/css2?family=Josefin+Sans:wght@400;600;700&family=Crimson+Text:wght@400;600&display=swap">
<style>
  :root {
    --brand-blue: #2152b3;
    --logo-blue: #3a6fd8;
    --paper-tint: #efeff2;
    --cut-line: #111111;
    --white: #ffffff;
    --ink: #1a1a1a;
    --photo-tone: #8c7865;
  }
  html, body {
    margin: 0;
    padding: 0;
    width: 1200px;
    height: 1200px;
    overflow: hidden;
    background: var(--white);
  }
  .dieline { display: block; width: 1200px; height: 1200px; }
  .cut { fill: none; stroke: var(--cut-line); stroke-width: 2; stroke-linejoin: miter; }
  .fold { fill: none; stroke: var(--cut-line); stroke-width: 2; stroke-dasharray: 5 5; }
  .flap-blank { fill: var(--white); stroke: var(--cut-line); stroke-width: 2; }
  .tint-field { fill: var(--paper-tint); }
  .blue-band { fill: var(--brand-blue); }
  .brand-dot { fill: var(--logo-blue); }
  .photo-slot { fill: var(--photo-tone); }
  .brand-name {
    font-family: "Josefin Sans", sans-serif;
    font-weight: 400;
    fill: var(--logo-blue);
    text-anchor: middle;
    letter-spacing: 1px;
  }
  .roast-title {
    font-family: "Josefin Sans", sans-serif;
    font-weight: 600;
    fill: var(--white);
    text-anchor: middle;
    letter-spacing: 3px;
    font-variant: small-caps;
  }
  .roast-detail {
    font-family: "Crimson Text", serif;
    fill: var(--white);
    text-anchor: middle;
  }
  .story-head {
    font-family: "Josefin Sans", sans-serif;
    font-weight: 700;
    font-size: 8px;
    fill: var(--ink);
    text-anchor: middle;
  }
  .story-body {
    font-family: "Crimson Text", serif;
    font-size: 6px;
    fill: var(--ink);
    text-anchor: middle;
  }
  .partner-name {
    font-family: "Josefin Sans", sans-serif;
    font-weight: 600;
    font-size: 8px;
    fill: var(--ink);
    text-anchor: middle;
  }
</style>
</head>
<body>
<svg class="dieline" viewBox="0 0 1500 1500" xmlns="http://www.w3.org/2000/svg">

  <!-- Top dust flap, front -->
  <g class="top-flap front-flap">
    <rect class="tint-field" x="155" y="405" width="405" height="220"/>
    <polygon class="blue-band" points="155,505 357,533 560,505 560,625 155,625"/>
    <circle class="brand-dot" cx="357" cy="458" r="17"/>
    <text class="brand-name" x="357" y="514" font-size="22">LUMO 317</text>
    <text class="roast-title" x="357" y="575" font-size="30">Signature Roast</text>
    <text class="roast-detail" x="357" y="601" font-size="12">Medium - Dark</text>
    <rect class="cut" x="155" y="405" width="405" height="220"/>
  </g>

  <!-- Top tuck, side -->
  <path class="flap-blank" d="M560,625 L560,545 L570,515 L770,515 L782,545 L782,625"/>

  <!-- Top dust flap, back -->
  <g class="top-flap back-flap">
    <rect class="tint-field" x="782" y="405" width="406" height="220"/>
    <polygon class="blue-band" points="782,505 985,533 1188,505 1188,625 782,625"/>
    <circle class="brand-dot" cx="985" cy="458" r="17"/>
    <text class="brand-name" x="985" y="514" font-size="22">LUMO 317</text>
    <text class="roast-title" x="985" y="575" font-size="30">Signature Roast</text>
    <text class="roast-detail" x="985" y="601" font-size="12">Medium - Dark</text>
    <rect class="cut" x="782" y="405" width="406" height="220"/>
  </g>

  <!-- Top tuck, second side -->
  <path class="flap-blank" d="M1188,625 L1188,545 L1200,533 L1205,468 L1393,468 L1398,533 L1410,545 L1410,625"/>

  <!-- Glue flap -->
  <path class="flap-blank" d="M155,627 L122,643 L122,930 L155,947"/>

  <!-- Front panel -->
  <g class="main-panel front-panel">
    <rect class="tint-field" x="155" y="625" width="405" height="322"/>
    <polygon class="blue-band" points="155,783 357,810 560,783 560,947 155,947"/>
    <circle class="brand-dot" cx="357" cy="692" r="30"/>
    <text class="brand-name" x="357" y="784" font-size="34">LUMO 317</text>
    <text class="roast-title" x="357" y="863" font-size="30">Signature Roast</text>
    <text class="roast-detail" x="357" y="897" font-size="12">Medium - Dark</text>
    <text class="roast-detail" x="357" y="915" font-size="12">24 Single Serve Pod</text>
  </g>

  <!-- Side panel with tear-off window -->
  <g class="main-panel side-panel">
    <rect class="tint-field" x="560" y="625" width="222" height="157"/>
    <rect class="blue-band" x="560" y="782" width="222" height="165"/>
    <circle class="brand-dot" cx="672" cy="670" r="14"/>
    <text class="brand-name" x="672" y="723" font-size="19">LUMO 317</text>
    <rect class="photo-slot" x="608" y="803" width="124" height="124" role="img" aria-label="Photo of a cup of black coffee seen from above"/>
  </g>

  <!-- Back panel -->
  <g class="main-panel back-panel">
    <rect class="tint-field" x="782" y="625" width="406" height="322"/>
    <polygon class="blue-band" points="782,783 985,810 1188,783 1188,947 782,947"/>
    <circle class="brand-dot" cx="985" cy="692" r="30"/>
    <text class="brand-name" x="985" y="784" font-size="34">LUMO 317</text>
    <text class="roast-title" x="985" y="862" font-size="30">Signature Roast</text>
    <text class="roast-detail" x="985" y="897" font-size="12">Medium - Dark</text>
    <text class="roast-detail" x="985" y="915" font-size="12">24 Single Serve Pod</text>
  </g>

  <!-- Story panel -->
  <g class="main-panel story-panel">
    <rect x="1188" y="625" width="222" height="322" fill="var(--white)"/>
    <circle class="brand-dot" cx="1299" cy="676" r="14"/>
    <text class="brand-name" x="1299" y="730" font-size="19">LUMO 317</text>

    <text class="story-head" x="1299" y="759">Premium Coffee</text>
    <text class="story-body" x="1299" y="770">We went directly to Honduran farms in search of high-grade,</text>
    <text class="story-body" x="1299" y="781">expertly grown and processed coffee. It is then carefully roasted,</text>
    <text class="story-body" x="1299" y="792">ensuring a full-bodied, well-balanced cup every time.</text>

    <text class="story-head" x="1299" y="811">Clean Water</text>
    <text class="story-body" x="1299" y="822">Millions of Hondurans live without access to clean water.</text>
    <text class="story-body" x="1299" y="833">Children miss school, illness is constant and the poverty cycle</text>
    <text class="story-body" x="1299" y="844">continues. With every box of Lumo 317 you provide over</text>
    <text class="story-body" x="1299" y="855">2000 gallons of clean water to those without it.</text>

    <text class="story-head" x="1299" y="874">Economic Empowerment</text>
    <text class="story-body" x="1299" y="885">We also work closely with Clear Spring Aid to source direct-trade</text>
    <text class="story-body" x="1299" y="896">coffee that helps hard working farmers leave extreme poverty,</text>
    <text class="story-body" x="1299" y="907">sometimes earning 10 times their previous income.</text>

    <text class="partner-name" x="1295" y="931">Clear Spring Aid</text>
  </g>

  <!-- Panel outline and crease lines -->
  <rect class="cut" x="155" y="625" width="1255" height="322"/>
  <line class="cut" x1="560" y1="625" x2="560" y2="947"/>
  <line class="cut" x1="782" y1="625" x2="782" y2="947"/>
  <line class="cut" x1="1188" y1="625" x2="1188" y2="947"/>

  <!-- Tear-away perforation -->
  <path class="fold" d="M430,405 L430,625 L560,755 L652,755 A20,20 0 0 1 692,755 L782,755 L913,625 L913,405"/>

  <!-- Bottom flaps -->
  <path class="flap-blank" d="M155,947 L167,1090 L298,1090 L316,1072 L316,1063 L444,1063 L462,1090 L560,1090 L560,947"/>
  <path class="cut" d="M560,947 L444,1063 M540,967 L560,987"/>
  <path class="flap-blank" d="M560,947 L572,1056 L658,1056 L782,947"/>
  <path class="flap-blank" d="M782,947 L794,1090 L926,1090 L944,1072 L944,1063 L1072,1063 L1090,1090 L1188,1090 L1188,947"/>
  <path class="cut" d="M1188,947 L1072,1063 M1168,967 L1188,987"/>
  <path class="flap-blank" d="M1188,947 L1200,1056 L1285,1056 L1410,947"/>
</svg>
</body>
</html>
```